Ferris Contracting LLC Business Card Design

I am looking for a creative and unique business card design. We are a commercial construction general contractor. With the name "FERRIS" Contracting, I am hoping to see some neat designs that correlate with the name.

```html
<!DOCTYPE html>
<html lang="en">
<head>
<meta charset="utf-8">
<title>Ferris Contracting LLC – Business Card</title>
<link href="https://fonts.googleapis.com/css2?family=Montserrat:wght@400;500;700&display=swap" rel="stylesheet">
<style>
  :root {
    --page: #ffffff;
    --navy-dark: #14284a;
    --navy: #1e3a63;
    --navy-light: #2a4d7c;
    --brand-blue: #1f8fe3;
    --text-light: #f2f6fb;
    --rule: #3f8fd6;
    --shadow: rgba(10, 20, 40, 0.28);
  }
  * { box-sizing: border-box; margin: 0; padding: 0; }
  html, body {
    width: 1200px;
    height: 800px;
    overflow: hidden;
    background: var(--page);
    font-family: "Montserrat", sans-serif;
  }
  .canvas {
    position: relative;
    width: 1200px;
    height: 800px;
  }
  .card {
    position: absolute;
    left: 224px;
    width: 750px;
    height: 358px;
    box-shadow: 6px 8px 16px var(--shadow);
    overflow: hidden;
  }
  .card--front { top: 23px; }
  .card--back  { top: 414px; }

  .card__backdrop {
    position: absolute;
    inset: 0;
    background: radial-gradient(ellipse at 55% 45%, var(--navy-light) 0%, var(--navy) 55%, var(--navy-dark) 100%);
  }

  .brand {
    position: absolute;
    left: 0;
    right: 0;
    top: 126px;
    text-align: center;
    color: var(--brand-blue);
    font-weight: 700;
  }
  .brand__name {
    display: block;
    font-size: 84px;
    line-height: 1;
    letter-spacing: 2px;
  }
  .brand__descriptor {
    display: block;
    margin-top: 14px;
    font-size: 24px;
    letter-spacing: 12px;
    padding-left: 12px;
  }

  .contact-list {
    position: absolute;
    left: 86px;
    top: 74px;
    width: 549px;
    list-style: none;
  }
  .contact-list__item {
    display: flex;
    align-items: center;
    gap: 14px;
    height: 54px;
    border-bottom: 1px solid var(--rule);
    color: var(--text-light);
    font-size: 21px;
    font-weight: 500;
    letter-spacing: 0.2px;
  }
  .contact-list__item:first-child { height: 53px; }
  .contact-list__icon {
    width: 24px;
    height: 24px;
    flex: none;
    fill: var(--text-light);
  }
  .contact-list__icon--outline {
    fill: none;
    stroke: var(--text-light);
    stroke-width: 1.5;
  }
</style>
</head>
<body>
<main class="canvas">

  <section class="card card--front" aria-label="Business card front">
    <div class="card__backdrop" role="img" aria-label="Navy blueprint-style architectural line drawing background"></div>
    <h1 class="brand">
      <span class="brand__name">FERRIS</span>
      <span class="brand__descriptor">CONTRACTING</span>
    </h1>
  </section>

  <section class="card card--back" aria-label="Business card back">
    <div class="card__backdrop" role="img" aria-label="Navy blueprint-style architectural line drawing background"></div>
    <ul class="contact-list">
      <li class="contact-list__item">
        <svg class="contact-list__icon" viewBox="0 0 24 24" aria-hidden="true"><path d="M12 2a7 7 0 0 0-7 7c0 5.2 7 13 7 13s7-7.8 7-13a7 7 0 0 0-7-7zm0 9.6A2.6 2.6 0 1 1 12 6.4a2.6 2.6 0 0 1 0 5.2z"/></svg>
        418 Ironworks Blvd., Dayton, OH 45402
      </li>
      <li class="contact-list__item">
        <svg class="contact-list__icon" viewBox="0 0 24 24" aria-hidden="true"><path d="M6.6 10.8a15.1 15.1 0 0 0 6.6 6.6l2.2-2.2a1 1 0 0 1 1-.25 11.4 11.4 0 0 0 3.6.57 1 1 0 0 1 1 1V20a1 1 0 0 1-1 1A17 17 0 0 1 3 4a1 1 0 0 1 1-1h3.5a1 1 0 0 1 1 1c0 1.25.2 2.45.57 3.6a1 1 0 0 1-.25 1z"/></svg>
        (937) 555-0148
      </li>
      <li class="contact-list__item">
        <svg class="contact-list__icon" viewBox="0 0 24 24" aria-hidden="true"><path d="M2 5h20v14H2z"/><path d="M3.5 6.5l8.5 6.5 8.5-6.5" fill="none" stroke="#1e3a63" stroke-width="1.6"/></svg>
        info@ferriscontracting.com
      </li>
      <li class="contact-list__item">
        <svg class="contact-list__icon contact-list__icon--outline" viewBox="0 0 24 24" aria-hidden="true"><circle cx="12" cy="12" r="9.5"/><ellipse cx="12" cy="12" rx="4" ry="9.5"/><path d="M2.5 12h19M4 7h16M4 17h16"/></svg>
        www.ferriscontracting.com
      </li>
    </ul>
  </section>

</main>
</body>
</html>
```